Need to design a business card with logo

Hellow
we are a company ,
PT KORAN MELATI JAYA
looking for design of name card.
what we do is property development and management.
design preferable professional corporate look and feel.
corporate. color, pantone colour 289
information required is
company name " Koran Melati Jaya"
person name eg " Peter Walsh"
person title eg "secret agent"
address: 12 heron lane , jakarta, indonesia
phone : +6221 5917264
mobile : 0812 463 518
email : peter@walshmail.example
website: www.peterwa.example
if you want to include logo in the design you are welcome and appreciated , or you can simply use the company name as the logo.
thanks
Target Market(s)
corporate , business person , show events, exhibition events ,etc
Industry/Entity Type
Business
Look and feel
Each slider illustrates characteristics of the customer's brand and the style your logo design should communicate.

```html
<!DOCTYPE html>
<html lang="en">
<head>
<meta charset="utf-8">
<title>Koran Melati Jaya – Business Card</title>
<link rel="stylesheet" href="https://fonts.googleapis.com/css2?family=Fira+Sans:wght@400;500;600&display=swap">
<style>
  :root {
    --page: #ffffff;
    --navy: #0e2240;
    --steel: #527790;
    --mist: #b5c6d1;
    --ink: #557a92;
  }
  html, body {
    margin: 0;
    padding: 0;
    width: 1200px;
    height: 720px;
    overflow: hidden;
    background: var(--page);
    font-family: "Fira Sans", sans-serif;
  }
  .canvas {
    position: relative;
    width: 1200px;
    height: 720px;
  }
  .card {
    position: absolute;
    left: 59px;
    top: 59px;
    width: 1063px;
    height: 539px;
    background: var(--navy);
    overflow: hidden;
  }
  .band-main {
    position: absolute;
    left: 0;
    top: 479px;
    width: 100%;
    height: 45px;
    background: var(--steel);
  }
  .band-light {
    position: absolute;
    left: 0;
    top: 524px;
    width: 100%;
    height: 15px;
    background: var(--mist);
  }
  .brand-mark {
    position: absolute;
    left: 64px;
    top: 150px;
    display: flex;
    align-items: center;
    gap: 16px;
    color: var(--mist);
    font-weight: 600;
    font-size: 34px;
    line-height: 44px;
    white-space: nowrap;
  }
  .brand-mark .square {
    width: 44px;
    height: 44px;
    background: var(--mist);
    flex: none;
  }
  .contact {
    position: absolute;
    right: 58px;
    text-align: right;
    color: var(--ink);
    white-space: nowrap;
  }
  .person { top: 34px; }
  .person .name {
    margin: 0;
    font-size: 40px;
    font-weight: 600;
    line-height: 48px;
  }
  .person .title {
    margin: 0;
    font-size: 28px;
    font-weight: 500;
    line-height: 28px;
  }
  .online {
    top: 126px;
    font-size: 22px;
    font-weight: 500;
    line-height: 30px;
  }
  .online p { margin: 0; }
  .company {
    top: 296px;
    margin: 0;
    font-size: 42px;
    font-weight: 600;
    line-height: 56px;
  }
  .address {
    top: 362px;
    font-size: 21px;
    font-weight: 400;
    line-height: 30px;
  }
  .address p { margin: 0; }
  .sep {
    display: inline-block;
    width: 1px;
    height: 24px;
    background: var(--ink);
    vertical-align: -5px;
    margin: 0 4px;
  }
</style>
</head>
<body>
<div class="canvas">
  <div class="card">
    <div class="band-main"></div>
    <div class="band-light"></div>

    <div class="brand-mark">
      <span class="square"></span>
      <span>Koran Melati Jaya</span>
    </div>

    <div class="contact person">
      <p class="name">Peter Walsh</p>
      <p class="title">secret agent</p>
    </div>

    <div class="contact online">
      <p>peter@walshmail.example</p>
      <p>www.peterwa.example</p>
    </div>

    <h1 class="contact company">Koran Melati Jaya</h1>

    <div class="contact address">
      <p>12 heron lane<span class="sep"></span>jakarta, indonesia</p>
      <p>+6221 5917264<span class="sep"></span>0812 463 518</p>
    </div>
  </div>
</div>
</body>
</html>
```